Business Card Design Project

Design is for the business card of a holistic, integral therapist. Design is required for front (colour / pattern) and back (white, with text as below).

Please prepare the design using placeholder text. I will work with the winning submission to complete the final information in the last iteration.

To give you a sense of her services a profile is below:
- I offer an integrative approach for effective relief of many issues such as anxiety, panic attacks, relationship difficulties, and health problems. In my counselling sessions I mainly use QBR {Quiet Balance Release } which taps into the body's energy system (meridians) to clear up blockages and limiting /distorted thinking and beliefs. I also work on expanding awareness as well as enhancing relationships.Clients have found the sessions life changing and report feeling lighter, clearer more empowered and connected to themselves and others.

Target Market(s)

Well educated, upper socioeconomic people seeking purpose and happiness in their lives.

Industry/Entity Type

Health

Requirements
Must have
• Must have the following text on front

First Name, Last Name
LLB, ND, Dip C
Counselling & Naturopathy
Quiet Balnce Release and Marlow Therapy

Adress 1 Line 1
Adress 1 Line 2

Adress 2 Line 1
Adress 2 Line 2

xxx.xxx@xxxxx.com

Tel: 0XXX XXX XXX

Must have the following text on reverse - which should be primarily white.

Next appointment
Date:
Time:
Nice to have
• Example colour palettes

http://www.huebinder.example/swatch/512093/velvet_lantern
http://www.huebinder.example/swatch/318420/Quiet_Orchard
http://www.huebinder.example/swatch/607215/Morning_Over_Tides

Example images that may be useful...
http://www.shopvarn.example/gp/product/images/4719205536/ref=dp_image_text_0?ie=UTF8&n=517302&s=books
http://www.shopvarn.example/gp/customer-media/product-gallery/6284019573/ref=cm_ciu_pdp_images_all
http://en.loreweb.example/wiki/File:Lotus_Grid_256bw.gif

```html
<!DOCTYPE html>
<html lang="en">
<head>
<meta charset="utf-8">
<title>Therapist Business Card – Front and Reverse</title>
<link rel="stylesheet" href="https://fonts.googleapis.com/css2?family=PT+Sans:wght@400;700&family=Italianno&display=swap">
<style>
  :root {
    --stage: #2b2b2b;
    --sea-green: #5fba99;
    --cream-text: #f4efa2;
    --paper: #fdfdf6;
    --rule: #5fba99;
    --ornament-gold: #efe9a0;
    --ornament-lime: #b8c43c;
  }
  html, body {
    margin: 0;
    padding: 0;
    width: 1200px;
    height: 852px;
    overflow: hidden;
    background: var(--stage);
  }
  .canvas {
    position: relative;
    width: 1200px;
    height: 852px;
    font-family: "PT Sans", "Helvetica Neue", Arial, sans-serif;
  }
  .card {
    position: absolute;
    width: 604px;
    height: 345px;
    box-sizing: border-box;
  }
  .card--front {
    left: 268px;
    top: 78px;
    background: var(--sea-green);
    color: var(--cream-text);
  }
  .card--back {
    left: 267px;
    top: 438px;
    background: var(--paper);
  }
  .mandala-emblem {
    position: absolute;
    left: 224px;
    top: 14px;
    width: 134px;
    height: 134px;
    border-radius: 50%;
    background: radial-gradient(circle, var(--ornament-lime) 0 22%, var(--ornament-gold) 24% 100%);
  }
  .practitioner-name {
    position: absolute;
    left: 0;
    right: 0;
    top: 152px;
    margin: 0;
    text-align: center;
    font-size: 21px;
    font-weight: 700;
    letter-spacing: 0.1px;
    padding-left: 0;
    transform: translateX(-14px);
  }
  .credentials {
    position: absolute;
    left: 0;
    right: 0;
    top: 180px;
    margin: 0;
    text-align: center;
    font-size: 16px;
    transform: translateX(-30px);
  }
  .services {
    position: absolute;
    left: 0;
    right: 0;
    top: 205px;
    margin: 0;
    text-align: center;
    font-family: "Italianno", "Brush Script MT", cursive;
    font-size: 22px;
    line-height: 23px;
  }
  .contact-row {
    position: absolute;
    left: 59px;
    top: 290px;
    display: flex;
    font-size: 14.5px;
    line-height: 20px;
  }
  .contact-column {
    margin: 0;
    font-style: normal;
  }
  .contact-column--address-one { width: 169px; }
  .contact-column--address-two { width: 170px; }
  .faint-mandala {
    position: absolute;
    left: 196px;
    top: 103px;
    width: 190px;
    height: 190px;
    border-radius: 50%;
    background: radial-gradient(circle, #f3f0c2 0 20%, #eaf2dc 22% 60%, #e4efe2 62% 100%);
    opacity: 0.8;
  }
  .appointment-banner {
    position: absolute;
    left: 86px;
    top: 27px;
    width: 427px;
    height: 34px;
  }
  .appointment-banner svg {
    position: absolute;
    inset: 0;
  }
  .appointment-title {
    position: absolute;
    left: 0;
    right: 0;
    top: -3px;
    margin: 0;
    text-align: center;
    font-family: "Italianno", "Brush Script MT", cursive;
    font-weight: 400;
    font-size: 34px;
    letter-spacing: 1.5px;
    color: var(--cream-text);
  }
  .writing-line {
    position: absolute;
    left: 38px;
    width: 520px;
    height: 0;
    border-top: 1.5px solid var(--rule);
  }
</style>
</head>
<body>
<main class="canvas">

  <section class="card card--front" aria-label="Business card front">
    <div class="mandala-emblem" role="img" aria-label="Decorative lotus mandala ornament in cream, gold and lime"></div>
    <h1 class="practitioner-name">Name Surname</h1>
    <p class="credentials">LLB, ND, Dip C</p>
    <p class="services">Counselling &amp; Naturopathy<br>Quiet Balnce Release and Marlow Therapy</p>
    <div class="contact-row">
      <address class="contact-column contact-column--address-one">Adress 1 Line 1<br>Adress 1 Line 2</address>
      <address class="contact-column contact-column--address-two">Adress 2 Line 1<br>Adress 2 Line 2</address>
      <address class="contact-column contact-column--reach">E:xxx.xxx@xxxxx.com<br>T: 0XXX XXX XXX</address>
    </div>
  </section>

  <section class="card card--back" aria-label="Business card reverse">
    <div class="faint-mandala" role="img" aria-label="Faint lotus mandala ornament watermark"></div>
    <div class="appointment-banner">
      <svg width="427" height="34" viewBox="0 0 427 34" aria-hidden="true">
        <polygon points="0,0 427,0 405,17 427,34 0,34 22,17" fill="#5fba99"/>
      </svg>
      <h2 class="appointment-title">Your Next Appointment</h2>
    </div>
    <div class="writing-line" style="top:95px"></div>
    <div class="writing-line" style="top:129px"></div>
    <div class="writing-line" style="top:164px"></div>
    <div class="writing-line" style="top:200px"></div>
    <div class="writing-line" style="top:236px"></div>
    <div class="writing-line" style="top:270px"></div>
    <div class="writing-line" style="top:305px"></div>
  </section>

</main>
</body>
</html>
```